Zielgruppe
Ich biete Employer-Branding-Beratung für mittelständische Unternehmen, d.h. ich entwickle für und mit meinen Kunden ihre Arbeitgebermarke und Arbeitgeberkommunikation, um leichter neue Mitarbeitende zu finden.
Meine Zielgruppe: mittelständische Unternehmen (1.000-4.000 Mitarbeitende), dort v.a. die Personalabteilung, meist Frauen
Aufgabenstellung
- Klappkarte im Format DIN lang. Die Karte soll sich dafür eignen, sie auf den Schreibtisch zu stellen.
- Corporate Design siehe Anhang. Darin ist bereits ein Entwurf für eine Karte enthalten. Der darf gern genau so übernommen werden. Ich freue mich aber auch über gute neue Entwürfe, die das CD aufgreifen.
- Seite 1: Logo & Zitat & Autor: 'Wege entstehen dadurch, dass man sie geht.' // Ottmar Riesel
- Seite 2: Text: Auf ein Jahr 2024 mit neuen Wegen!
- Seite 3: leer
- Seite 4: Adresse/Kontaktdaten:
Mareike Lindqvist
Die Talentmarken-Lotsin
Weidenkamp 41
10437 Berlin
T +49 (15 27) 390 52 17
E ml@die-talentmarken-lotsin.de
Hinweis: Die Karte wird in durchsichtigen Umschlägen verschickt, die Adresse sollte so kontrastreich sein, dass man sie auch durch den Umschläge sehen kann, falls Briefe zurück kommen.

```html
<!DOCTYPE html>
<html lang="de">
<head>
<meta charset="utf-8">
<title>Klappkarte DIN lang – Die Talentmarken-Lotsin</title>
<link rel="stylesheet" href="https://fonts.googleapis.com/css2?family=Open+Sans:ital,wght@0,400;0,600;0,700;0,800;1,400;1,700;1,800&display=swap">
<style>
  :root {
    --backdrop: #7b7b7b;
    --plum: #4f0035;
    --mauve: #8a4d6e;
    --blush: #c9a9bb;
    --amber: #f0a030;
    --white: #ffffff;
    --heading-plum: #551040;
    --year-plum: #7e4a68;
    --ridge: #e9d8e1;
  }
  html, body {
    margin: 0;
    padding: 0;
    width: 803px;
    height: 1200px;
    overflow: hidden;
    background: var(--backdrop);
  }
  .sheet {
    position: relative;
    width: 803px;
    height: 1200px;
    font-family: "Open Sans", Arial, sans-serif;
  }
  .card-panel {
    position: absolute;
    top: 338px;
    width: 370px;
    height: 523px;
    display: block;
  }
  .card-outside { left: 21px; }
  .card-inside { left: 412px; }

  .fill-blush { fill: var(--blush); }
  .fill-plum { fill: var(--plum); }
  .fill-mauve { fill: var(--mauve); }
  .ring { fill: none; stroke: var(--mauve); stroke-width: 45; }

  .contact-name { fill: var(--white); font-weight: 700; font-size: 17px; letter-spacing: 0.5px; }
  .contact-line { fill: var(--white); font-weight: 400; font-size: 16px; letter-spacing: 0.3px; }
  .contact-small { fill: var(--white); font-weight: 400; font-size: 12.5px; }
  .icon-dot { fill: var(--amber); }
  .icon-glyph { fill: none; stroke: var(--white); stroke-width: 1.2; }

  .brand-name { fill: var(--white); font-weight: 400; font-size: 24px; letter-spacing: 1.5px; }
  .brand-dot { fill: none; stroke: var(--white); stroke-width: 3; }
  .quote { fill: var(--white); font-style: italic; font-weight: 400; font-size: 23px; }
  .quote-author { fill: var(--amber); font-weight: 700; font-size: 18px; }
  .arc-url { fill: var(--white); font-weight: 600; font-size: 12.5px; letter-spacing: 2.2px; }

  .paper { fill: var(--white); }
  .greeting-kicker { fill: var(--heading-plum); font-weight: 700; font-size: 31px; letter-spacing: 11px; }
  .greeting-year { fill: var(--year-plum); font-weight: 800; font-size: 172px; letter-spacing: -9px; }
  .greeting-tagline { fill: var(--amber); font-style: italic; font-weight: 800; font-size: 55px; letter-spacing: -1px; }
  .burst { fill: var(--ridge); }
</style>
</head>
<body>
<main class="sheet">

  <!-- Außenseite: Rückseite (Kontakt, gedreht) über Titelseite -->
  <svg class="card-panel card-outside" viewBox="0 0 690 976" aria-label="Außenseite der Klappkarte">
    <rect class="fill-blush" x="0" y="0" width="690" height="976" role="img" aria-label="Hellrosa Fläche mit geschwungenem Linienmuster"/>
    <rect class="fill-plum" x="345" y="0" width="345" height="976"/>
    <rect class="fill-plum" x="170" y="245" width="175" height="510"/>
    <circle class="fill-plum" cx="345" cy="245" r="220"/>
    <circle class="fill-plum" cx="345" cy="755" r="220"/>
    <circle class="ring" cx="345" cy="245" r="197.5"/>
    <circle class="ring" cx="345" cy="755" r="197.5"/>
    <rect class="fill-mauve" x="125" y="245" width="45" height="510"/>
    <rect class="fill-mauve" x="518" y="0" width="44" height="976"/>

    <g class="back-contact" transform="rotate(180 345 245)">
      <text class="contact-name" x="345" y="147" text-anchor="middle">MAREIKE LINDQVIST</text>
      <text class="contact-line" x="345" y="173" text-anchor="middle">DIE TALENTMARKEN-</text>
      <text class="contact-line" x="345" y="197" text-anchor="middle">LOTSIN</text>
      <text class="contact-line" x="345" y="221" text-anchor="middle">WEIDENKAMP 41</text>
      <text class="contact-line" x="345" y="245" text-anchor="middle">10437 BERLIN</text>

      <g class="icon-phone">
        <circle class="icon-dot" cx="345" cy="272" r="7"/>
        <path class="icon-glyph" d="M342 268 q0 6 6 8"/>
      </g>
      <text class="contact-small" x="345" y="298" text-anchor="middle">+49 (15 27) 390 52 17</text>

      <g class="icon-mail">
        <circle class="icon-dot" cx="345" cy="321" r="7"/>
        <rect class="icon-glyph" x="341" y="318.5" width="8" height="5.5"/>
        <path class="icon-glyph" d="M341 318.5 l4 3 l4 -3"/>
      </g>
      <text class="contact-small" x="345" y="347" text-anchor="middle">ml@die-talentmarken-lotsin.de</text>

      <g class="icon-web">
        <circle class="icon-dot" cx="345" cy="370" r="7"/>
        <circle class="icon-glyph" cx="345" cy="370" r="4"/>
        <path class="icon-glyph" d="M341 370 h8 M345 366 v8"/>
      </g>
      <text class="contact-small" x="345" y="396" text-anchor="middle">die-talentmarken-lotsin.de</text>
    </g>

    <g class="front-title">
      <circle class="brand-dot" cx="252" cy="672" r="12"/>
      <text class="brand-name" x="276" y="665">DIE TALENT-</text>
      <text class="brand-name" x="276" y="693">MARKEN-LOTSIN</text>
      <text class="quote" x="345" y="786" text-anchor="middle">Wege entstehen dadurch,</text>
      <text class="quote" x="345" y="817" text-anchor="middle">dass man sie geht.</text>
      <text class="quote-author" x="345" y="857" text-anchor="middle">Ottmar Riesel</text>

      <path id="url-arc" d="M 150.5 789.3 A 197.5 197.5 0 0 0 443.8 926" fill="none"/>
      <text class="arc-url" dy="5"><textPath href="#url-arc">DIE-TALENTMARKEN-LOTSIN.DE</textPath></text>
    </g>
  </svg>

  <!-- Innenseite: Neujahrsgruß -->
  <svg class="card-panel card-inside" viewBox="0 0 690 976" aria-label="Innenseite der Klappkarte">
    <rect class="paper" x="0" y="0" width="690" height="976"/>

    <g role="img" aria-label="Zierliche Feuerwerkssterne in Pflaumenlinien">
      <circle class="burst" cx="105" cy="92" r="44"/>
      <circle class="burst" cx="610" cy="85" r="56"/>
      <circle class="burst" cx="140" cy="286" r="40"/>
      <circle class="burst" cx="555" cy="280" r="40"/>
    </g>

    <text class="greeting-kicker" x="350" y="102" text-anchor="middle">AUF EIN JAHR</text>
    <text class="greeting-year" x="346" y="250" text-anchor="middle">2024</text>
    <text class="greeting-tagline" x="350" y="315" text-anchor="middle">mit neuen</text>
    <text class="greeting-tagline" x="350" y="370" text-anchor="middle">Wegen!</text>

    <defs>
      <linearGradient id="ridge-fade" x1="0" y1="0" x2="0" y2="1">
        <stop offset="0" stop-color="#e9d8e1"/>
        <stop offset="1" stop-color="#f6eef2"/>
      </linearGradient>
    </defs>
    <path d="M0 320 C60 330 90 400 140 380 C190 360 220 360 260 420 C330 410 420 400 520 330 C600 350 650 380 690 390 L690 490 L0 490 Z"
          fill="url(#ridge-fade)" role="img" aria-label="Linienzeichnung einer Berg- und Dünenlandschaft"/>
  </svg>

</main>
</body>
</html>
```